Word Cloud Graphic Wallpaper design

The following sentences need to be put together in an ai file of the size : 70" wide and 108" high . This will be used as a wall paper. Inspirational image is attached. (We have also attached a rough idea showing you the wall it would go one- DO NOT REPLICATE THE LAYOUT OF THE SENTENCES-This only shows you how we will be using your file)

Sentences are:

Dentistry is not Expensive Neglect is!
Smiles are free but they are worth alot.
Don't Forget to Floss!
Put on your best SMILE everyday!
Be the reason someone smiles today.
Let your SMILE CHANGE THE WORLD, don't let the world change your smile.
Make your smile your signature accessory!

These should be in different fonts (clean modern fonts only please- no cursive or busy fonts - Helvetica Neue, Arial and fonts such as those are preferred) and sizes and should be easily legible (minimum font height 4"). Repetitions are ok if needed to fill space.

Font styles to use
Sans Serif

Requirements
Must have
• hese should be in different fonts (clean modern fonts only please- no cursive or busy fonts - Helvetica Neue, Arial and fonts such as those) and sizes and should be easily legible (minimum font height 4"). Repetitions are ok if needed to fill space.
Should not have
• Cursive, busy, fonts.

```html
<!DOCTYPE html>
<html lang="en">
<head>
<meta charset="UTF-8">
<title>Smile Word Wallpaper</title>
<link href="https://fonts.googleapis.com/css2?family=Baumans&display=swap" rel="stylesheet">
<style>
  :root {
    --page-bg: #dfe7ef;
    --poster-red: #8a0c02;
    --line-red: #ec1119;
    --line-orange: #f28a0c;
    --line-amber: #f5c30c;
    --line-yellow: #ffee00;
    --line-lemon: #fbe76a;
    --line-cream: #fde8b4;
    --line-white: #ffffff;
  }
  html, body {
    margin: 0;
    padding: 0;
    width: 1200px;
    height: 800px;
    overflow: hidden;
    background: var(--page-bg);
  }
  .wallpaper {
    position: absolute;
    left: 353px;
    top: 20px;
    width: 493px;
    height: 760px;
    overflow: hidden;
    background: var(--poster-red);
    font-family: "Baumans", "Century Gothic", sans-serif;
  }
  .quote {
    position: absolute;
    left: 34px;
    margin: 0;
    white-space: nowrap;
    font-weight: 400;
  }
  .quote--dentistry { top: 17px;  font-size: 40px; line-height: 47px; color: var(--line-red); }
  .quote--free      { top: 130px; font-size: 40px; line-height: 47px; color: var(--line-orange); }
  .quote--floss     { top: 242px; font-size: 39px; line-height: 47px; color: var(--line-amber); }
  .quote--best      { top: 308px; font-size: 52px; line-height: 61px; color: var(--line-yellow); }
  .quote--reason    { top: 448px; font-size: 36px; line-height: 41px; color: var(--line-lemon); }
  .quote--world     { top: 550px; font-size: 22px; line-height: 32px; color: var(--line-cream); }
  .quote--signature { top: 629px; font-size: 41px; line-height: 46px; color: var(--line-white); }
</style>
</head>
<body>
  <main class="wallpaper">
    <p class="quote quote--dentistry">Dentistry is not<br>Expensive Neglect is!</p>
    <p class="quote quote--free">Smiles are free but<br>they are worth A lot.</p>
    <p class="quote quote--floss">Don’t Forget to Floss!</p>
    <p class="quote quote--best">Put on your best<br>SMILE everyday!</p>
    <p class="quote quote--reason">Be the reason someone<br>smiles today.</p>
    <p class="quote quote--world">Let your SMILE CHANGE THE WORLD,<br>don’t let the world change your smile.</p>
    <p class="quote quote--signature">Make your smile your<br>signature accessory!</p>
  </main>
</body>
</html>
```